Startup Drone Platform Company business card

We are needing a business card design for our employees. We are a startup drone platform. We are looking for a business card that has our logo on one side, with the employee/company details on the opposite side. We are looking for something that is very eye catching, modern, and bold.

Target Market(s)

This will target both drone pilots and drone businesses, along with all the industries that could utilize drone services (aerial video, aerial photos, inspections, 3d mapping, etc).

Industry/Entity Type

Business

```html
<!DOCTYPE html>
<html lang="en">
<head>
<meta charset="utf-8">
<title>Skyhop Aerial – Business Card</title>
<link rel="stylesheet" href="https://fonts.googleapis.com/css2?family=Montserrat:wght@400&family=Open+Sans:wght@400&display=swap">
<style>
  :root {
    --backdrop: #4b4b4b;
    --card-dark: #060709;
    --card-light: #ffffff;
    --teal: #3bbdc6;
    --ink: #111111;
    --white: #ffffff;
  }
  html, body {
    margin: 0;
    width: 1200px;
    height: 1200px;
    overflow: hidden;
    background: var(--backdrop);
  }
  .card {
    position: absolute;
    left: 189px;
    width: 823px;
    height: 466px;
    border-radius: 28px;
    overflow: hidden;
  }
  .card--front {
    top: 90px;
    background: var(--card-dark);
  }
  .card--back {
    top: 646px;
    background: var(--card-light);
  }
  .brand {
    position: absolute;
    left: 0;
    right: 0;
    top: 170px;
    display: flex;
    flex-direction: column;
    align-items: center;
    gap: 18px;
  }
  .brand__mark {
    width: 34px;
    height: 34px;
    border-radius: 50%;
    border: 4px solid var(--white);
    box-sizing: border-box;
  }
  .brand__name {
    margin: 0;
    font-family: "Montserrat", sans-serif;
    font-weight: 400;
    color: var(--white);
    font-size: 30px;
    letter-spacing: 0.55em;
    padding-left: 0.55em;
    line-height: 1.45;
    text-align: center;
  }
  .back-disc {
    position: absolute;
    left: -152px;
    top: 33px;
    width: 400px;
    height: 400px;
    border-radius: 50%;
    background: var(--card-dark);
  }
  .contact {
    position: absolute;
    left: 320px;
    top: 152px;
    font-family: "Open Sans", sans-serif;
    color: var(--ink);
  }
  .contact__name {
    margin: 0;
    font-size: 31px;
    font-weight: 400;
    color: var(--teal);
    line-height: 1.1;
  }
  .contact__role {
    margin: 2px 0 22px;
    font-size: 20px;
  }
  .contact__list {
    list-style: none;
    margin: 0;
    padding: 0;
  }
  .contact__item {
    display: flex;
    align-items: center;
    font-size: 20px;
    height: 28px;
  }
  .contact__icon {
    width: 22px;
    height: 22px;
    margin-right: 14px;
    flex: none;
  }
</style>
</head>
<body>
  <section class="card card--front">
    <div class="brand">
      <span class="brand__mark"></span>
      <p class="brand__name">SKYHOP<br>AERIAL</p>
    </div>
  </section>

  <section class="card card--back">
    <div class="back-disc"></div>
    <div class="contact">
      <h1 class="contact__name">Daniel Reeve</h1>
      <p class="contact__role">Managing Partner</p>
      <ul class="contact__list">
        <li class="contact__item">
          <svg class="contact__icon" viewBox="0 0 24 24" aria-hidden="true">
            <path d="M2 9c0-3 4-5 10-5s10 2 10 5v2h-5V9H7v2H2z" fill="#3bbdc6"/>
            <path d="M6 12h12l2 8H4z" fill="#3bbdc6"/>
            <circle cx="12" cy="16" r="2.6" fill="#fff"/>
          </svg>
          +00 (00) 000-0000
        </li>
        <li class="contact__item">
          <svg class="contact__icon" viewBox="0 0 24 24" aria-hidden="true">
            <rect x="2" y="5" width="20" height="14" fill="#3bbdc6"/>
            <path d="M2 5l10 8 10-8M2 19l7-7M22 19l-7-7" stroke="#fff" stroke-width="1.5" fill="none"/>
          </svg>
          dreeve@skyhopaerial.com
        </li>
        <li class="contact__item">
          <svg class="contact__icon" viewBox="0 0 24 24" aria-hidden="true">
            <g fill="none" stroke="#3bbdc6" stroke-width="1.6">
              <circle cx="12" cy="12" r="10"/>
              <ellipse cx="12" cy="12" rx="4.5" ry="10"/>
              <path d="M2 12h20M4 7h16M4 17h16"/>
            </g>
          </svg>
          www.skyhopaerial.com
        </li>
      </ul>
    </div>
  </section>
</body>
</html>
```